Project Manager Business Card for Top Architectural Firm

Update and design a stunning Senior Project Manager Business Card

MARCO T. DRUMMOND II
Senior Project Manager

H A L C Y O N
A R C H I T E C T U R E L L C.
www.HalcyonGrandEstates.example
4127 NW 52nd Ter. Suite 2308
Miami, FL 33148
C: (305) 555-0184
mdrummond.halcyongrandestates@mailbox.example

Looking to have the logo to be UV Spot ink printed and to be prominent.

Target Market(s)

High end real estate architecture construction

Industry/Entity Type

Architect

Contact Information for Business Card

MARCO T. DRUMMOND II
Senior Project Manager

H A L C Y O N
Miami, FL 33148
C: (305) 555-0184

Font styles to use
Sans Serif

Colors

Designer to choose colors to be used in the design.

Requirements
Must have
• Prominent Logo

```html
<!DOCTYPE html>
<html lang="en">
<head>
<meta charset="utf-8">
<title>Halcyon Architecture LLC – Business Card</title>
<link rel="stylesheet" href="https://fonts.googleapis.com/css2?family=Arimo:wght@400;700&display=swap">
<style>
  :root {
    --backdrop: #2b2b2b;
    --panel-dark: #050505;
    --panel-dark-edge: #2e2e2e;
    --panel-light: #ffffff;
    --panel-light-shade: #e4e4e4;
    --brand-blue: #1b84c4;
    --ink: #1e1e1e;
    --rule: #8a8a8a;
    --mark-grey: #6f6f6f;
  }
  html, body {
    margin: 0;
    width: 1200px;
    height: 997px;
    overflow: hidden;
    background: var(--backdrop);
    font-family: "Arimo", Arial, sans-serif;
  }
  .canvas {
    position: relative;
    width: 1200px;
    height: 997px;
  }
  .card {
    position: absolute;
    left: 150px;
    top: 241px;
    width: 900px;
    height: 514px;
    display: flex;
    box-shadow: 0 18px 40px rgba(0,0,0,.55);
  }
  .card__brand {
    width: 380px;
    background: linear-gradient(160deg, var(--panel-dark) 0%, var(--panel-dark) 45%, var(--panel-dark-edge) 100%);
    display: flex;
    flex-direction: column;
    justify-content: center;
    align-items: center;
    gap: 18px;
  }
  .brand__dot {
    width: 70px;
    height: 70px;
    border-radius: 50%;
    background: var(--mark-grey);
    margin-bottom: 14px;
  }
  .brand__name,
  .brand__sub {
    margin: 0;
    color: var(--mark-grey);
    font-weight: 400;
    white-space: pre;
    text-align: center;
  }
  .brand__name { font-size: 52px; letter-spacing: 2px; }
  .brand__sub  { font-size: 15px; letter-spacing: 1px; }
  .card__details {
    flex: 1;
    background: linear-gradient(135deg, var(--panel-light) 0%, var(--panel-light) 55%, var(--panel-light-shade) 100%);
    padding: 70px 52px 0 60px;
    text-align: right;
    color: var(--ink);
  }
  .details__block { padding: 14px 0; }
  .details__rule {
    border: 0;
    border-top: 1.5px solid var(--rule);
    margin: 0 0 0 30px;
  }
  .person__name, .company__name, .contact__web {
    margin: 0;
    color: var(--brand-blue);
    font-weight: 700;
  }
  .person__name  { font-size: 22px; }
  .company__name { font-size: 21px; }
  .person__title, .company__address, .contact__line {
    margin: 4px 0 0;
    font-size: 19px;
  }
  .contact__web { font-size: 23px; margin-top: 8px; }
  .contact__line--email { font-size: 17px; }
</style>
</head>
<body>
  <main class="canvas">
    <article class="card">
      <section class="card__brand">
        <div class="brand__dot" aria-hidden="true"></div>
        <p class="brand__name">H A L C Y O N</p>
        <p class="brand__sub">A R C H I T E C T U R E  L L C.</p>
      </section>
      <section class="card__details">
        <div class="details__block">
          <p class="person__name">MARCO T. DRUMMOND II</p>
          <p class="person__title">Senior Project Manager</p>
        </div>
        <hr class="details__rule">
        <div class="details__block">
          <p class="company__name">HALCYON ARCHITECTURE LLC.</p>
          <p class="company__address">4127 NW 52nd Ter. Suite 2308</p>
          <p class="company__address">Miami, FL 33148</p>
        </div>
        <hr class="details__rule">
        <div class="details__block">
          <p class="contact__line">(305) 555-0184</p>
        </div>
        <hr class="details__rule">
        <div class="details__block">
          <p class="contact__line contact__line--email">mdrummond.halcyongrandestates@mailbox.example</p>
          <p class="contact__web">www.HalcyonGrandEstates.example</p>
        </div>
      </section>
    </article>
  </main>
</body>
</html>
```